【仕様】
・B5(182×257㎜)
・背幅は9㎜です(修正有)
・本文は横書きですので左綴じとなります。
・カバー(表1、表4、背表紙):4C(フルカラー)
・表紙(表1、表4、背表紙):1C
・扉:1C
・袖は10㎜
・帯のようなデザインは問題ありませんが、帯そのものをつける予定はありません。

※表紙・扉のデザインはカバーデザインに基づいたもので、「書名」「編者名」「社名(ロゴマーク)」だけが入っているもので結構です。
【デザインについて】
・書籍の内容は堅いですが、保育士をめざす学生がこの書籍を使って学びたくなるような、そして親しみをもてるデザインを希望します。

・イラスト等を加えていただいても結構です。

・書名等に用いる書体の指定はございません。

・書名、編者名等のデザインに盛り込む内容(文字)は添付ファイルを参照してください。
シンプル 複雑
単色 カラフル
暗い 明るい
日常 高級
遊び心 厳粛
未来的 伝統的
女性的 男性的
特に指定はありません。
• イラストレーター形式 (.ai)
【仕様】の項目で、袖の長さを10㎜と表記しておりましたが、110㎜に訂正いたします。

①学生が好みそうな非常にかわいらしく、やわらかいイメージ。
②「言葉」の「 」の部分の葉っぱのデザイン。
③「保育内容」とコピー文の部分の色がカラフルで、きれいなデザイン。
④テキストという堅さをやわらげてくれるデザイン。

この度は多くのご提案をありがとうございました。
それぞれに様々な思いを込めて作成いただいたことを、とてもうれしく感じました。感謝申し上げます。
今回採用できなかった提案の中にも、他の書籍のカバーとして採用したいと思うものが多くありました。
今後も様々な書籍で依頼をさせていただく予定でおりますので、また是非ご応募いただき、皆さんのお力をお借りしながら、一つの書籍という作品を世に送り出せればと考えておりますので、どうぞよろしくお願い申し上げます。

```html
<!DOCTYPE html>
<html lang="ja">
<head>
<meta charset="utf-8">
<title>保育士をまなぶ人の保育領域「言葉」</title>
<link rel="stylesheet" href="https://fonts.googleapis.com/css2?family=M+PLUS+Rounded+1c:wght@500;800&family=Noto+Sans+JP:wght@400;500;700&display=swap">
<style>
  :root {
    --paper: #ffffff;
    --edge: #d9d9d9;
    --pink-light: #ef6b9f;
    --pink-deep: #e5307a;
    --sky: #2ea7e0;
    --ink: #444444;
    --white: #ffffff;
  }
  * { margin: 0; padding: 0; box-sizing: border-box; }
  html, body { width: 849px; height: 1200px; overflow: hidden; background: var(--paper); }
  .cover {
    position: relative;
    width: 849px; height: 1200px;
    border: 2px solid var(--edge);
    font-family: "Noto Sans JP", sans-serif;
    color: var(--ink);
  }
  .bubbles { position: absolute; inset: 0; }
  .editor {
    position: absolute; left: 678px; top: 120px;
    writing-mode: vertical-rl;
    font-size: 22px; font-weight: 500; letter-spacing: 0.1em; line-height: 1;
    display: flex; align-items: center; gap: 10px;
  }
  .editor::before {
    content: ""; width: 18px; height: 18px; border-radius: 50%;
    background: var(--sky);
  }
  .title-line {
    position: absolute; left: 232px;
    font-family: "M PLUS Rounded 1c", sans-serif;
    font-weight: 800; font-size: 66px; line-height: 1;
    color: var(--white); white-space: nowrap;
  }
  .title-line.one { top: 188px; }
  .title-line.two { top: 257px; }
  .title-line.three { top: 326px; }
  .title-sub {
    position: absolute; left: 425px; width: 350px; top: 448px;
    text-align: center;
    font-family: "M PLUS Rounded 1c", sans-serif;
    font-weight: 800; font-size: 70px; line-height: 1;
    color: var(--white); white-space: nowrap;
  }
  .parts {
    position: absolute; left: 235px; top: 620px;
    display: flex; align-items: center; gap: 11px;
  }
  .part {
    width: 70px; height: 28px; background: var(--sky); color: var(--white);
    font-size: 13px; font-weight: 500;
    display: flex; align-items: center; justify-content: center;
  }
  .parts-note { font-size: 15px; line-height: 1.3; margin-left: 4px; white-space: nowrap; }
  .appendix {
    position: absolute; left: 232px; top: 671px;
    display: flex; align-items: flex-start; gap: 6px;
  }
  .appendix-label {
    width: 139px; height: 42px; background: var(--sky); color: var(--white);
    font-size: 11px; line-height: 1.5; font-weight: 500;
    padding: 4px 7px; white-space: nowrap;
  }
  .appendix-list { font-size: 10.5px; line-height: 1.75; padding-top: 2px; white-space: nowrap; }
  .appendix-list span { margin-right: 10px; }
  .appendix-list span::before { content: "●"; color: var(--sky); }
  .publisher {
    position: absolute; left: 0; right: 0; top: 1057px;
    display: flex; justify-content: center; align-items: center; gap: 6px;
    font-size: 15px; font-weight: 700; color: var(--sky);
  }
  .publisher::before {
    content: ""; width: 16px; height: 16px; border-radius: 50%;
    background: var(--sky);
  }
</style>
</head>
<body>
<div class="cover">
  <svg class="bubbles" width="849" height="1200" viewBox="0 0 849 1200" aria-hidden="true">
    <path fill="var(--pink-light)" d="M437 113 C600 113 671 200 671 318 C671 430 600 524 437 524 C400 524 370 520 340 512 L249 566 L285 490 C230 460 204 400 204 318 C204 200 275 113 437 113 Z"/>
    <path fill="var(--pink-deep)" d="M600 405 C700 405 775 440 775 485 C775 520 752 545 718 556 L741 594 L680 563 C655 566 628 566 600 566 C500 566 425 530 425 485 C425 440 500 405 600 405 Z"/>
  </svg>

  <div class="editor">森田 春香 編</div>

  <h1>
    <span class="title-line one">保育士を</span>
    <span class="title-line two">まなぶ人の</span>
    <span class="title-line three">保育領域</span>
    <span class="title-sub">「言葉」</span>
  </h1>

  <div class="parts">
    <div class="part">基礎編</div>
    <div class="part">実践編</div>
    <div class="part">実技編</div>
    <div class="part">発展編</div>
    <p class="parts-note">の4編構成で<br>ステップアップ学習が可能</p>
  </div>

  <div class="appendix">
    <p class="appendix-label">学びをより深めるため<br>巻末に付録を掲載</p>
    <p class="appendix-list">
      <span>心・身体・言葉の発達表</span><span>主な園行事の紹介</span><br>
      <span>パペットを制作してみよう</span><span>幼稚園教育要領(抄)</span><span>保育所保育指針(抄)</span>
    </p>
  </div>

  <div class="publisher">はなの書房</div>
</div>
</body>
</html>
```